BrevoLunt Business Card Design Project

We are looking for a modern, clean business card design for our new company. We are a consulting firm focused on the financial services market providing management and IT consulting to banks, insurance companies, etc. Please include our company logo and company contact information from the attached file in the design. Two versions of the logo are attached, either version is acceptable. Logos are available in other file formats if needed. We would like to include the contact information for both our UK and US offices as well as the following information for each individual card holder: Name, position/title, address, phone number and e-mail address.
Updates
Project Deadline Extended
Reason: A last minute trip over seas has prevented us from finalizing the decision. A decision will be made this week. We apologize for the inconvenience.
Industry/Entity Type
Business
Contact Information for Business Card
Company logo.
Company locations and phone numbers for both the US and UK offices.
Company URL.
Cardholder Name
Cardholder Position/title
Cardholder Address
Cardholder Phone Number
Cardholder e-mail Address
Look and feel
Each slider illustrates characteristics of the customer's brand and the style your logo design should communicate.

```html
<!DOCTYPE html>
<html lang="en">
<head>
<meta charset="utf-8">
<title>BrevoLunt Partners – Business Card</title>
<link href="https://fonts.googleapis.com/css2?family=Roboto:wght@300;400;700&display=swap" rel="stylesheet">
<style>
  :root {
    --backdrop: #d8d5d1;
    --card-light: #ebebeb;
    --navy: #12284a;
    --navy-band: #27375a;
    --grey-band: #5b5b5b;
    --text-grey: #6a6a6a;
    --text-dark: #3d3d3d;
    --white: #ffffff;
  }
  html, body {
    margin: 0;
    padding: 0;
    width: 1200px;
    height: 987px;
    overflow: hidden;
    background: var(--backdrop);
    font-family: "Roboto", Arial, sans-serif;
  }
  .stage {
    position: relative;
    width: 1200px;
    height: 987px;
  }
  .card {
    position: absolute;
    left: 250px;
    width: 700px;
    height: 400px;
    box-shadow: 0 4px 14px rgba(0,0,0,0.22);
    overflow: hidden;
  }
  /* Front side */
  .card-front {
    top: 60px;
    background: var(--card-light);
  }
  .brand {
    position: absolute;
    left: 48px;
    top: 52px;
    display: flex;
    align-items: center;
    gap: 12px;
  }
  .brand-mark {
    width: 26px;
    height: 26px;
    background: var(--navy);
  }
  .brand-name {
    font-weight: 700;
    font-size: 36px;
    color: var(--navy);
    letter-spacing: -0.5px;
  }
  .offices {
    position: absolute;
    left: 52px;
    top: 140px;
    font-weight: 300;
    font-size: 15px;
    line-height: 22px;
    color: var(--text-grey);
  }
  .office + .office { margin-top: 14px; }
  .holder {
    position: absolute;
    left: 400px;
    top: 62px;
  }
  .holder-name {
    font-size: 20px;
    font-weight: 400;
    color: var(--navy);
    margin: 0;
  }
  .holder-title {
    font-size: 13px;
    font-weight: 300;
    color: var(--text-grey);
    margin: 4px 0 26px;
  }
  .contact-list {
    list-style: none;
    margin: 0;
    padding: 0;
    font-size: 13px;
    font-weight: 300;
    color: var(--text-dark);
  }
  .contact-list li {
    display: flex;
    align-items: center;
    gap: 8px;
    height: 22px;
  }
  .contact-icon {
    width: 13px;
    height: 13px;
    flex: none;
  }
  .edge-band {
    position: absolute;
    left: 0;
    bottom: 0;
    width: 100%;
    height: 34px;
    display: flex;
  }
  .edge-band-navy { flex: 58; background: var(--navy-band); }
  .edge-band-grey { flex: 42; background: var(--grey-band); }
  /* Back side */
  .card-back {
    top: 527px;
    background: var(--navy);
    display: flex;
    flex-direction: column;
    align-items: center;
    justify-content: center;
  }
  .brand-back {
    display: flex;
    align-items: center;
    gap: 16px;
  }
  .brand-back .brand-mark {
    width: 34px;
    height: 34px;
    background: var(--white);
  }
  .brand-back .brand-name {
    color: var(--white);
    font-size: 48px;
  }
  .back-url {
    margin-top: 34px;
    font-size: 15px;
    font-weight: 400;
    color: var(--white);
  }
</style>
</head>
<body>
<main class="stage">

  <section class="card card-front" aria-label="Business card front">
    <div class="brand">
      <span class="brand-mark"></span>
      <span class="brand-name">BrevoLunt Partners</span>
    </div>

    <div class="offices">
      <div class="office">
        418 N Calder Ave, Suite 204-210<br>
        Brookfield UT 84120<br>
        United States
      </div>
      <div class="office">
        14-16 Marlow Street<br>
        London E2 4RP<br>
        Great Britain
      </div>
    </div>

    <div class="holder">
      <h1 class="holder-name">Daniel Hartwell</h1>
      <p class="holder-title">Manager</p>
      <ul class="contact-list">
        <li>
          <svg class="contact-icon" viewBox="0 0 14 14"><circle cx="7" cy="7" r="7" fill="var(--navy)"/><path d="M4.5 4 L6 4 L6.6 5.6 L5.8 6.3 Q6.6 7.8 7.8 8.4 L8.5 7.6 L10 8.2 L10 9.6 Q6.5 10 4.2 6 Z" fill="#fff"/></svg>
          (555) 214-7730 (US)
        </li>
        <li>
          <svg class="contact-icon" viewBox="0 0 14 14"><circle cx="7" cy="7" r="7" fill="var(--navy)"/><path d="M4.5 4 L6 4 L6.6 5.6 L5.8 6.3 Q6.6 7.8 7.8 8.4 L8.5 7.6 L10 8.2 L10 9.6 Q6.5 10 4.2 6 Z" fill="#fff"/></svg>
          +44 7700 900418 (UK)
        </li>
        <li>
          <svg class="contact-icon" viewBox="0 0 14 14"><circle cx="7" cy="7" r="7" fill="var(--navy)"/><rect x="3.5" y="4.5" width="7" height="5" fill="none" stroke="#fff" stroke-width="1"/><path d="M3.5 4.5 L7 7.3 L10.5 4.5" fill="none" stroke="#fff" stroke-width="1"/></svg>
          daniel@brevoluntpartners.com
        </li>
        <li>
          <svg class="contact-icon" viewBox="0 0 14 14"><circle cx="7" cy="7" r="7" fill="var(--navy)"/><circle cx="7" cy="7" r="3.6" fill="none" stroke="#fff" stroke-width="0.9"/><ellipse cx="7" cy="7" rx="1.6" ry="3.6" fill="none" stroke="#fff" stroke-width="0.9"/><line x1="3.4" y1="7" x2="10.6" y2="7" stroke="#fff" stroke-width="0.9"/></svg>
          www.brevoluntpartners.com
        </li>
      </ul>
    </div>

    <div class="edge-band">
      <span class="edge-band-navy"></span>
      <span class="edge-band-grey"></span>
    </div>
  </section>

  <section class="card card-back" aria-label="Business card back">
    <div class="brand-back">
      <span class="brand-mark"></span>
      <span class="brand-name">BrevoLunt Partners</span>
    </div>
    <div class="back-url">www.brevoluntpartners.com</div>
  </section>

</main>
</body>
</html>
```